Stationery for General Contracting Company
Company focuses in renovation for home & offices with integrated smart home solutions
Professional
Marcel Okafor
342 Fernwick Lane Oakhollow, NJ 07612
marcel@BrightBuildHQ.example
www.BrightBuildHQ.example
Residential Professional Hospitality Houses of Worship Smart Technologies Interior & Exterior Bathroom & Kitchen Basements & Attics

```html
<!DOCTYPE html>
<html lang="en">
<head>
<meta charset="utf-8">
<title>BrightBuildHQ Business Card</title>
<link rel="stylesheet" href="https://fonts.googleapis.com/css2?family=Arimo:wght@400;700&display=swap">
<style>
  :root {
    --backdrop: #ececec;
    --card: #e2e2e2;
    --orange: #e0601f;
    --ink: #1e1e1e;
    --brand-ink: #5a5a5a;
    --mark-ring: #ffffff;
  }
  * { margin: 0; padding: 0; box-sizing: border-box; }
  html, body {
    width: 1200px; height: 876px; overflow: hidden;
    background: var(--backdrop);
    font-family: "Arimo", Arial, sans-serif;
  }
  .canvas { position: relative; width: 1200px; height: 876px; }
  .card {
    position: absolute; width: 640px; height: 365px;
    background: var(--card); overflow: hidden;
  }
  .card-front { left: 280px; top: 44px; }
  .card-back { left: 280px; top: 468px; }
  .card-shape { position: absolute; inset: 0; width: 100%; height: 100%; }
  .brand { position: absolute; display: flex; align-items: center; }
  .brand-dot {
    border-radius: 50%; background: var(--orange);
    border: 6px solid var(--mark-ring); flex: none;
  }
  .brand-name { font-weight: 700; color: var(--brand-ink); white-space: nowrap; }
  .card-front .brand { left: 190px; top: 120px; }
  .card-front .brand-dot { width: 84px; height: 84px; margin-right: 12px; }
  .card-front .brand-name { font-size: 28px; }
  .card-back .brand { left: 328px; top: 70px; }
  .card-back .brand-dot { width: 50px; height: 50px; margin-right: 10px; border-width: 4px; }
  .card-back .brand-name { font-size: 20px; }
  .person-name {
    position: absolute; left: 26px; top: 176px;
    font-size: 30px; color: var(--ink); font-weight: 400;
  }
  .person-name .given { font-weight: 700; }
  .contact-list { position: absolute; left: 26px; top: 222px; list-style: none; }
  .contact-item {
    display: flex; align-items: center; height: 32px;
    font-size: 19px; color: var(--ink);
  }
  .contact-icon { width: 18px; height: 18px; margin-right: 14px; fill: var(--ink); flex: none; }
</style>
</head>
<body>
<main class="canvas">
  <section class="card card-front" aria-label="Card front">
    <svg class="card-shape" viewBox="0 0 640 365" aria-hidden="true">
      <rect width="640" height="365" fill="var(--orange)"/>
      <polygon points="222,66 640,66 640,365 0,365" fill="var(--card)"/>
    </svg>
    <div class="brand">
      <span class="brand-dot"></span>
      <span class="brand-name">BrightBuildHQ.example</span>
    </div>
  </section>

  <section class="card card-back" aria-label="Card back">
    <svg class="card-shape" viewBox="0 0 640 365" aria-hidden="true">
      <polygon points="0,88 140,26 640,340 640,365 612,365 140,46 0,106" fill="var(--orange)"/>
    </svg>
    <div class="brand">
      <span class="brand-dot"></span>
      <span class="brand-name">BrightBuildHQ.example</span>
    </div>
    <h1 class="person-name"><span class="given">Marcel</span> Okafor</h1>
    <ul class="contact-list">
      <li class="contact-item">
        <svg class="contact-icon" viewBox="0 0 24 24" aria-hidden="true"><path d="M6.6 10.8a15 15 0 0 0 6.6 6.6l2.2-2.2a1 1 0 0 1 1-.25 11.4 11.4 0 0 0 3.6.57 1 1 0 0 1 1 1V20a1 1 0 0 1-1 1A17 17 0 0 1 3 4a1 1 0 0 1 1-1h3.5a1 1 0 0 1 1 1c0 1.25.2 2.45.57 3.57a1 1 0 0 1-.25 1z"/></svg>
        555 014 2277
      </li>
      <li class="contact-item">
        <svg class="contact-icon" viewBox="0 0 24 24" aria-hidden="true"><path d="M2 5h20v14H2zM4 7v.5l8 5 8-5V7zm0 2.8V17h16V9.8l-8 5z"/></svg>
        marcel@BrightBuildHQ.example
      </li>
      <li class="contact-item">
        <svg class="contact-icon" viewBox="0 0 24 24" aria-hidden="true"><path d="M4 3l15 7-6 2 5 8-2.5 1.5-5-8L6 18z"/></svg>
        www.BrightBuildHQ.example
      </li>
      <li class="contact-item">
        <svg class="contact-icon" viewBox="0 0 24 24" aria-hidden="true"><path d="M12 2a7 7 0 0 0-7 7c0 5.2 7 13 7 13s7-7.8 7-13a7 7 0 0 0-7-7zm0 9.5A2.5 2.5 0 1 1 12 6.5a2.5 2.5 0 0 1 0 5z"/></svg>
        342 Fernwick Lane Oakhollow, NJ 07612
      </li>
    </ul>
  </section>
</main>
</body>
</html>
```